E-commerce Website needs category banner

What we need for our category banner is a clean, predominately black design that showcases the product we are trying to sell (currently only 1), and a few subtle gradients that follow the pattern set by previous designs.

An example will be provided to showcase what we want.

It needs to say:
Outdoor Motion Detection Lighting in large, clear font similar to the example provided.
Updates

Please ensure dimensions are as follows: 980x300

Target Market(s)

Senior citizens, businesses, homeowners, families, etc

Industry/Entity Type

Product

Font styles to use
Sans Serif

Requirements
Must have
• It needs to say:
Outdoor Motion Detection Lighting in large, clear font similar to the example provided
980x300 is the required size!
Should not have
• Too much going on- clean and simple please (no crazy fonts, logos, etc)

```html
<!DOCTYPE html>
<html lang="en">
<head>
<meta charset="utf-8">
<title>Outdoor Motion Detection Lighting</title>
<link rel="stylesheet" href="https://fonts.googleapis.com/css2?family=Bebas+Neue&display=swap">
<style>
  :root {
    --bg-core: #4b4b4b;
    --bg-mid: #2a2a2a;
    --bg-edge: #0b0b0b;
    --floor-top: #3a3a3a;
    --floor-bottom: #050505;
    --headline: #ffffff;
    --product-light: #f2f2f2;
    --product-shade: #bdbdbd;
  }
  html, body {
    margin: 0;
    padding: 0;
    overflow: hidden;
    background: #000;
  }
  .banner {
    position: relative;
    width: 1200px;
    height: 367px;
    overflow: hidden;
    background:
      radial-gradient(ellipse 70% 85% at 55% 40%, var(--bg-core) 0%, var(--bg-mid) 45%, var(--bg-edge) 100%);
  }
  .banner__floor {
    position: absolute;
    left: 0;
    right: 0;
    top: 290px;
    bottom: 0;
    background: linear-gradient(180deg, var(--floor-top) 0%, #1a1a1a 25%, var(--floor-bottom) 100%);
  }
  .banner__floor::before {
    content: "";
    position: absolute;
    left: 0;
    right: 0;
    top: 0;
    height: 2px;
    background: linear-gradient(90deg, transparent, rgba(255,255,255,0.18) 40%, rgba(255,255,255,0.18) 70%, transparent);
  }
  .headline {
    position: absolute;
    left: 24px;
    top: 55px;
    margin: 0;
    font-family: "Bebas Neue", "Arial Narrow", sans-serif;
    font-weight: 400;
    color: var(--headline);
    text-shadow: 0 3px 6px rgba(0,0,0,0.6);
    line-height: 1;
    z-index: 2;
  }
  .headline__line {
    display: block;
    white-space: nowrap;
  }
  .headline__line--first {
    font-size: 93px;
    letter-spacing: 5px;
  }
  .headline__line--second {
    font-size: 104px;
    letter-spacing: 0.5px;
    margin-top: -9px;
  }
  .product {
    position: absolute;
    border-radius: 46% 46% 40% 40%;
    background: radial-gradient(ellipse at 35% 30%, var(--product-light) 0%, #dcdcdc 55%, var(--product-shade) 100%);
    box-shadow: 0 8px 18px rgba(0,0,0,0.5);
  }
  .product--double {
    left: 748px;
    top: 24px;
    width: 194px;
    height: 242px;
  }
  .product--single {
    left: 960px;
    top: 20px;
    width: 190px;
    height: 254px;
  }
</style>
</head>
<body>
  <section class="banner">
    <div class="banner__floor"></div>
    <h1 class="headline">
      <span class="headline__line headline__line--first">Outdoor Motion</span>
      <span class="headline__line headline__line--second">Detection Lighting</span>
    </h1>
    <div class="product product--double" role="img" aria-label="White wall-mounted motion sensor spotlight with two LED lamps"></div>
    <div class="product product--single" role="img" aria-label="White wall-mounted motion sensor spotlight with one LED lamp"></div>
  </section>
</body>
</html>
```